Halvern Aviation Group - "Coming Soon" Main Company Webpage

Design a main webpage that can be posted while a fully functional website is constructed. The design should be created to convey a sense of luxury and exclusivity. The main page should contain only one photo as the background. The photo I believe to show "luxury" and "Exclusivity" is listed as "Global Luxury Photo". I have included two other photos as well to aid in providing a variety of presentations.
The "Member PQTR" logo should appear somewhere on the main page but be less prevalent than the main company logo. "Coming Soon" should also appear to convey that a website is being constructed.
Tabs for the website:
- Aircraft Management
- Aircraft Sales
- Pilot Services
- Charter
- Flight Training

```html
<!DOCTYPE html>
<html lang="en">
<head>
<meta charset="UTF-8">
<title>Halvern Aviation Group – Coming Soon</title>
<link rel="stylesheet" href="https://fonts.googleapis.com/css2?family=Mulish:wght@400;500;800&display=swap">
<style>
  :root{
    --brand-blue:#0a64b4;
    --ink:#111111;
    --white:#ffffff;
    --footer-bg:#000000;
    --footer-ink:#e6e6e6;
    --photo-top:#6f7a8c;
    --photo-mid:#b9bec8;
    --photo-low:#e9eaee;
  }
  *{margin:0;padding:0;box-sizing:border-box}
  html,body{width:1200px;height:576px;overflow:hidden;background:var(--white)}
  body{font-family:"Mulish",sans-serif;color:var(--ink);position:relative}

  .site-header{position:absolute;left:0;top:0;width:1200px;height:93px;background:var(--white);z-index:2;box-shadow:0 6px 18px rgba(0,0,0,.06)}
  .brand{position:absolute;left:161px;top:22px;width:240px;display:flex;align-items:center;gap:10px;
    font-weight:800;font-size:20px;letter-spacing:.6px;color:var(--brand-blue);text-transform:uppercase;line-height:24px}
  .brand-dot{flex:none;width:14px;height:14px;background:var(--brand-blue);border-radius:50%}
  .brand-name{display:block;max-width:190px}
  .main-nav{position:absolute;left:451px;top:37px;display:flex;white-space:nowrap}
  .main-nav a{font-size:13.6px;font-weight:500;color:var(--ink);text-decoration:none;line-height:18px;letter-spacing:.2px}
  .main-nav a+a{margin-left:36px}

  .intro{position:absolute;left:0;top:93px;width:600px;height:438px;background:var(--white)}
  .intro-title{position:absolute;left:160px;top:155px;font-size:40px;font-weight:800;color:var(--brand-blue);letter-spacing:-.5px;line-height:1}
  .intro-sub{position:absolute;left:161px;top:203px;font-size:22.5px;font-weight:500;line-height:1}
  .intro-text{position:absolute;left:161px;top:238px;width:390px;font-size:13.4px;line-height:20.5px;font-weight:500}

  .membership{position:absolute;left:161px;top:372px;display:flex;align-items:flex-end;gap:10px}
  .membership-mark{width:44px;height:30px;border-radius:50%;background:var(--brand-blue)}
  .membership-label{display:flex;flex-direction:column;font-weight:500;color:var(--ink);line-height:1}
  .membership-label small{font-size:10px;margin-bottom:4px}
  .membership-label span{font-size:24px;letter-spacing:3px}

  .hero-photo{position:absolute;left:600px;top:93px;width:600px;height:438px;
    background:linear-gradient(165deg,var(--photo-top) 0%,var(--photo-mid) 35%,var(--photo-low) 60%,#d4d6dc 85%,#8d9097 100%)}

  .site-footer{position:absolute;left:0;top:531px;width:1200px;height:45px;background:var(--footer-bg);
    display:flex;align-items:center;justify-content:center;color:var(--footer-ink);font-size:13px;letter-spacing:.3px}
</style>
</head>
<body>
  <header class="site-header">
    <div class="brand"><span class="brand-dot"></span><span class="brand-name">Halvern Aviation Group</span></div>
    <nav class="main-nav">
      <a href="#">Aircraft Management</a>
      <a href="#">Aircraft Sales</a>
      <a href="#">Pilot Services</a>
      <a href="#">Charter</a>
      <a href="#">Flight Training</a>
    </nav>
  </header>

  <section class="intro">
    <h1 class="intro-title">COMING SOON...</h1>
    <h2 class="intro-sub">WEBSITE IS UNDER CONSTRUCTION</h2>
    <p class="intro-text">Ut enim ad minim veniam quis nostrud exercitation ullamco aute laboris nisi ut aliquip ex ea commodo consequat.</p>
    <div class="membership">
      <div class="membership-mark"></div>
      <div class="membership-label"><small>member of</small><span>PQTR</span></div>
    </div>
  </section>

  <div class="hero-photo" role="img" aria-label="Close-up photo of a white private business jet nose and engines under a cloudy sky"></div>

  <footer class="site-footer">© 2023 HALVERN AVIATION GROUP. All Rights Reserved.</footer>
</body>
</html>
```